Opening soon Zest Marlowe Grooming Specialist

I need a flyer to be posted through peoples letter boxes for the opening of my dog grooming salon. It needs to be bright, bold and eye catching. Something cool and modern but not overly masculine or too feminine. Text to include salon phone number 07918465203, 50% discouunt for 1st 2 weeks of opening, owned and operated by ex-military dog handler and trainer and larch and fenwick level 3 professional dog groomer.

```html
<!DOCTYPE html>
<html lang="en">
<head>
<meta charset="utf-8">
<title>Zest Marlowe Grooming Specialist – Opening Flyer</title>
<link rel="stylesheet" href="https://fonts.googleapis.com/css2?family=Arimo:wght@400;700&display=swap">
<style>
  :root {
    --brand-red: #e31c25;
    --brand-red-dark: #b0111a;
    --ink: #141414;
    --white: #ffffff;
    --deck-light: #dcd9d5;
    --deck-mid: #bdb6ae;
    --coat-white: #ece8e3;
    --coat-tan: #b07a4c;
    --coat-dark: #3a2a20;
  }
  html, body {
    margin: 0;
    padding: 0;
    width: 849px;
    height: 1200px;
    overflow: hidden;
    background: #ffffff;
  }
  .flyer {
    position: relative;
    width: 849px;
    height: 1200px;
    overflow: hidden;
    font-family: "Arimo", Arial, sans-serif;
    background: var(--brand-red);
  }
  .hero-photo {
    position: absolute;
    left: 0;
    top: 80px;
    width: 849px;
    height: 1010px;
    background:
      radial-gradient(ellipse 150px 170px at 575px 480px, var(--coat-white) 0%, rgba(236,232,227,0.6) 45%, transparent 100%),
      radial-gradient(ellipse 300px 300px at 575px 420px, var(--coat-tan) 0%, rgba(176,122,76,0.75) 50%, transparent 100%),
      radial-gradient(ellipse 420px 560px at 560px 560px, var(--coat-dark) 0%, rgba(58,42,32,0.85) 45%, rgba(58,42,32,0.25) 80%, transparent 100%),
      linear-gradient(165deg, var(--deck-light) 0%, #cdc8c2 50%, var(--deck-mid) 100%);
  }
  .flyer__bands {
    position: absolute;
    inset: 0;
    width: 849px;
    height: 1200px;
  }
  .brand {
    position: absolute;
    left: 30px;
    top: 30px;
    width: 340px;
    text-align: center;
    color: var(--ink);
  }
  .brand__name {
    display: block;
    font-weight: 700;
    font-size: 150px;
    line-height: 200px;
    letter-spacing: -4px;
  }
  .brand__tagline {
    display: block;
    margin-top: 38px;
    font-weight: 400;
    font-size: 28px;
    line-height: 32px;
  }
  .contact {
    position: absolute;
    top: 28px;
    right: 30px;
    display: flex;
    align-items: center;
    gap: 16px;
    color: var(--white);
    font-weight: 700;
    font-size: 52px;
    letter-spacing: 1px;
    text-shadow: 2px 2px 4px rgba(0,0,0,0.45);
  }
  .contact__icon {
    width: 34px;
    height: 44px;
    filter: drop-shadow(2px 2px 3px rgba(0,0,0,0.4));
  }
  .offer {
    position: absolute;
    left: 27px;
    top: 695px;
    width: 345px;
    height: 324px;
    box-sizing: border-box;
    border-radius: 34px;
    background: linear-gradient(180deg, var(--brand-red) 0%, var(--brand-red-dark) 100%);
    box-shadow: 0 4px 14px rgba(0,0,0,0.35);
    color: var(--white);
    font-weight: 700;
    text-align: center;
    text-shadow: 2px 3px 4px rgba(0,0,0,0.45);
    padding-top: 14px;
  }
  .offer__figure {
    display: block;
    font-size: 145px;
    line-height: 130px;
    letter-spacing: -3px;
  }
  .offer__detail {
    display: block;
    font-size: 46px;
    line-height: 48px;
  }
  .offer__highlight {
    display: block;
    font-size: 74px;
    line-height: 72px;
  }
  .credentials {
    position: absolute;
    left: 0;
    right: 0;
    top: 1106px;
    margin: 0;
    color: var(--white);
    font-weight: 700;
    font-size: 23px;
    line-height: 27px;
    letter-spacing: 1.8px;
    text-align: center;
  }
</style>
</head>
<body>
  <main class="flyer">
    <div class="hero-photo" role="img" aria-label="Photograph of a happy tricolour beagle puppy sitting on a grey wooden deck, looking up with its mouth open"></div>

    <svg class="flyer__bands" viewBox="0 0 849 1200" aria-hidden="true">
      <path fill="#e31c25" d="M0 0 H849 V128 C700 112 560 102 420 100 C280 98 140 98 0 100 Z"/>
      <path fill="#e31c25" d="M0 1062 C160 1072 320 1080 480 1078 C640 1074 760 1056 849 1042 V1200 H0 Z"/>
    </svg>

    <div class="brand">
      <span class="brand__name">Zest</span>
      <span class="brand__tagline">Marlowe Grooming<br>Specialist</span>
    </div>

    <div class="contact">
      <svg class="contact__icon" viewBox="0 0 24 30" aria-hidden="true">
        <path fill="#ffffff" d="M6 2 C4 2 2 4 2 7 C2 17 8 26 15 28 C17 29 19 28 20 26 L21 23 C21 22 20 21 19 21 L15 20 C14 20 13 21 13 22 C10 20 8 15 8 12 C9 12 10 11 10 10 L10 5 C10 4 9 3 8 3 Z"/>
      </svg>
      <span class="contact__phone">07918465203</span>
    </div>

    <div class="offer">
      <span class="offer__figure">50%</span>
      <span class="offer__detail">discount for<br>1st 2 weeks of</span>
      <span class="offer__highlight">opening</span>
    </div>

    <p class="credentials">owned and operated by ex-military dog handler and trainer<br>and larch and fenwick level 3 professional dog groomer.</p>
  </main>
</body>
</html>
```